Hip Music Management Co. BIz Card

I have a logo (attached) the back side of the card should the full logo on the entire card- that's it. The front side of the card should show the logo somewhere, keeping with the 4 different shades of blue. The front side of the card can be a white background with logo and colored typeface for all info. Pretty simple.

Target Market(s)

I manage and produce a whole bunch of major label and indie artists.

Industry/Entity Type

Management

Contact Information for Business Card

Velmarra Sound Collective (logo)
Dale Wortheny
President
www.velmarrasoundcollective.com
dale@velmarrasoundcollective.com
+1 415.287.6192
718 Copperfield Lane
Larkstone Hollow, NY 12874

Requirements
Must have
• Entire logo on back side. White background on front- unless you provide something more interesting.
Nice to have
• On the front of the card if you choose a white backgound, if possible take my logo without the blue background (over white) that would be cool.

```html
<!DOCTYPE html>
<html lang="en">
<head>
<meta charset="utf-8">
<title>Velmarra Sound Collective – Business Card</title>
<link href="https://fonts.googleapis.com/css2?family=Roboto+Condensed:wght@700&family=Roboto:wght@300;400&display=swap" rel="stylesheet">
<style>
  :root {
    --page: #eef0f4;
    --navy-deep: #0b1a44;
    --navy: #14306a;
    --navy-dark-band: #1b2250;
    --blue-band: #1a78c4;
    --teal: #2bb0c8;
    --sky: #6ab6ea;
    --white: #ffffff;
    --title-grey: #dfe6f2;
  }
  * { box-sizing: border-box; margin: 0; padding: 0; }
  html, body { width: 1200px; height: 1000px; overflow: hidden; }
  body { background: var(--page); position: relative; font-family: "Roboto", Arial, sans-serif; }

  .card {
    position: absolute;
    width: 665px;
    height: 380px;
    overflow: hidden;
    box-shadow: 0 6px 18px rgba(0, 0, 0, 0.25);
  }

  /* Back side: full wordmark on navy */
  .card--back { left: 60px; top: 70px; }
  .card--back .texture {
    position: absolute; inset: 0;
    background: radial-gradient(ellipse at 45% 40%, var(--navy) 0%, var(--navy-deep) 75%);
  }
  .card--back .wordmark {
    position: absolute; inset: 0;
    display: flex; align-items: center; justify-content: center;
    gap: 16px;
    font-family: "Roboto Condensed", "Arial Narrow", sans-serif;
    font-weight: 700;
    font-size: 44px;
    color: var(--sky);
    text-align: center;
  }
  .wordmark .dot {
    width: 22px; height: 22px; border-radius: 50%;
    background: var(--sky); flex: none;
  }

  /* Front side: white top, curved bands, navy contact panel */
  .card--front { left: 475px; top: 540px; background: var(--white); }
  .card--front .bands { position: absolute; inset: 0; }
  .card--front .wordmark-front {
    position: absolute; left: 88px; top: 38px;
    display: flex; align-items: center; gap: 12px;
    font-family: "Roboto Condensed", "Arial Narrow", sans-serif;
    font-weight: 700;
    font-size: 34px;
    color: var(--teal);
  }
  .wordmark-front .dot {
    width: 16px; height: 16px; border-radius: 50%;
    background: var(--teal); flex: none;
  }
  .person { position: absolute; left: 74px; top: 200px; color: var(--white); }
  .person__name {
    font-family: "Roboto Condensed", "Arial Narrow", sans-serif;
    font-weight: 700; font-size: 34px; letter-spacing: 0.5px;
    text-transform: uppercase;
  }
  .person__title { font-weight: 300; font-size: 21px; color: var(--title-grey); margin-top: 2px; }
  .contact {
    position: absolute; right: 40px; top: 206px;
    text-align: right; color: var(--white);
    font-size: 16px; line-height: 24px; font-weight: 400;
  }
  .contact .gap { height: 8px; }
</style>
</head>
<body>

  <section class="card card--back" aria-label="Card back">
    <div class="texture" role="img" aria-label="Navy halftone dot texture background"></div>
    <div class="wordmark"><span class="dot"></span>Velmarra Sound Collective</div>
  </section>

  <section class="card card--front" aria-label="Card front">
    <svg class="bands" viewBox="0 0 665 380" width="665" height="380" aria-hidden="true">
      <defs>
        <radialGradient id="panelTone" cx="40%" cy="60%" r="80%">
          <stop offset="0" stop-color="#183a78"/>
          <stop offset="1" stop-color="#0d1f4c"/>
        </radialGradient>
      </defs>
      <path d="M0,142 Q360,140 665,52 L665,380 L0,380 Z" fill="var(--blue-band)"/>
      <path d="M0,158 Q360,156 665,76 L665,380 L0,380 Z" fill="var(--navy-dark-band)"/>
      <path d="M0,178 Q360,176 665,100 L665,380 L0,380 Z" fill="url(#panelTone)"/>
    </svg>

    <div class="wordmark-front"><span class="dot"></span>Velmarra Sound Collective</div>

    <div class="person">
      <div class="person__name">Dale Wortheny</div>
      <div class="person__title">President</div>
    </div>

    <div class="contact">
      <div>www.velmarrasoundcollective.com</div>
      <div>dale@velmarrasoundcollective.com</div>
      <div>+1 415.287.6192</div>
      <div class="gap"></div>
      <div>718 Copperfield Lane</div>
      <div>Larkstone Hollow, NY 12874</div>
    </div>
  </section>

</body>
</html>
```